Technology solutions catalog

Were looking for a catalogue to supplement our website and corporate branding.

Our website will give you a good understanding of our products and services as well as our theme.

Our base colour and logo is red, white and grey.

www.voltrane.com.au

The aim of the catalogue is to showcase our business IT services & solutions. This will be a mix of education about the new solutions available to small and medium business today and how these solutions can increase productivity.

We would also like tip sections

This isn't all about selling but also about educating SMB's of the new and exciting IT solutions available today and having them book a free consult with us to discuss further about how we can help the business.

Solutions and area's that the catalogue will need to cover include

Front Cover -
-About us section, with our business contact information (1st page)
- Introduction. (2nd page)
-Communication Solutions - this includes Email, IP phones and business IT networks (2 pages)
- Data & Storage solutions (2 pages)
- Hardware (1 pages)
- Business IT health check list (1 page)
- Services and support offering (2 pages)
- Software & Popular cloud solutions (2 pages)
- Website / E-commerce solutions (2 pages)
Back cover

Based on two pages per solution the whole catalogue will be around 14 pages.

We don't need any text content done. We would like Headings on pages including page numbers. Footer please.

We're looking for a template that we can have our designer finish off by adding in some further product and service image and text.

Thank you for your consideration

Target Market(s)

IT for small and medium businesses

Industry/Entity Type

Supplement

Requirements
Must have
• Size A4
• Design supplied in Adobe indesign so we can edit and add our text and content
• Clean design

```html
<!DOCTYPE html>
<html lang="en">
<head>
<meta charset="utf-8">
<title>Voltrane — Technology Solutions Catalogue Cover</title>
<link rel="stylesheet" href="https://fonts.googleapis.com/css2?family=Open+Sans:wght@400;700;800&display=swap">
<style>
  :root {
    --backdrop: #e6e6e6;
    --page-top: #f7f7f7;
    --page-bottom: #e4e4e4;
    --brand-red: #d94457;
    --red-deep: #b30c22;
    --red-soft: #cf2a3d;
    --outline: #ffffff;
    --caption: #6a6a6a;
  }
  html, body {
    margin: 0;
    width: 1200px;
    height: 900px;
    overflow: hidden;
    background: var(--backdrop);
  }
  .cover {
    position: absolute;
    left: 20px;
    top: 40px;
    width: 1160px;
    height: 820px;
    overflow: hidden;
    background: linear-gradient(160deg, var(--page-top) 0%, var(--page-bottom) 100%);
    box-shadow: 0 2px 6px rgba(0,0,0,0.12);
  }
  .cover-art { display: block; }
  .wordmark {
    font-family: "Open Sans", sans-serif;
    font-weight: 800;
    fill: var(--brand-red);
  }
  .caption {
    font-family: "Open Sans", sans-serif;
    font-weight: 400;
    font-size: 9px;
    fill: var(--caption);
  }
  .frame-line { fill: none; stroke: var(--outline); stroke-width: 1.5; }
  .logo-tile { fill: #f4f4f4; stroke: var(--outline); stroke-width: 1.5; }
</style>
</head>
<body>
  <main class="cover">
    <svg class="cover-art" width="1160" height="820" viewBox="0 0 1160 820" xmlns="http://www.w3.org/2000/svg">
      <defs>
        <linearGradient id="red-fill" x1="0" y1="0" x2="1" y2="1">
          <stop offset="0" stop-color="var(--red-soft)"/>
          <stop offset="1" stop-color="var(--red-deep)"/>
        </linearGradient>
      </defs>

      <!-- Title wordmark -->
      <text class="wordmark" x="1090" y="150" font-size="64" text-anchor="end">Voltrane</text>

      <!-- Large outline tile -->
      <polygon class="frame-line" points="360,500 580,720 360,940 140,720"/>

      <!-- Logo tile -->
      <polygon class="logo-tile" points="360,390 470,500 360,610 250,500"/>
      <text class="wordmark" x="360" y="511" font-size="30" text-anchor="middle">Voltrane</text>

      <!-- Photo tiles -->
      <g role="img" aria-label="Photo of a software screen with a colourful spreadsheet">
        <polygon points="800,170 910,280 800,390 690,280" fill="#d9dde2"/>
      </g>
      <g role="img" aria-label="Photo of a smiling man working at a computer screen">
        <polygon points="690,280 800,390 765,425 615,425 580,390" fill="#b7c2cc"/>
      </g>
      <polygon points="615,425 765,425 690,500" fill="#ffffff"/>
      <text class="caption" x="690" y="444" text-anchor="middle">Business IT made simple</text>
      <text class="caption" x="690" y="456" text-anchor="middle">for growing teams</text>

      <g role="img" aria-label="Photo of a businessman with colourful sticky notes">
        <polygon points="360,610 470,720 360,830 250,720" fill="#c9c2b4"/>
      </g>
      <g role="img" aria-label="Photo of a woman working in an office">
        <polygon points="580,610 690,720 580,830 470,720" fill="#a9b3bf"/>
      </g>
      <g role="img" aria-label="Photo of a smiling man with glasses">
        <polygon points="1130,310 1240,420 1130,530 1020,420" fill="#d8c2b0"/>
      </g>

      <!-- Red decorative tiles -->
      <g role="img" aria-label="Decorative red faceted tile">
        <polygon points="470,500 580,610 470,720 360,610" fill="url(#red-fill)"/>
      </g>
      <g role="img" aria-label="Decorative red faceted tile">
        <polygon points="800,390 910,500 800,610 690,500" fill="url(#red-fill)"/>
      </g>
      <g role="img" aria-label="Decorative red faceted tile">
        <polygon points="690,500 800,610 690,720 580,610" fill="url(#red-fill)"/>
      </g>
    </svg>
  </main>
</body>
</html>
```